Gedric's Lager BEER CAN

DESIGN USE
This is not for a business, it's for a (thoughtful) gift to my father. The design is going to be on a personalised beer can, so it will be a cylindrical shape. Basically, I'm giving him a few six-packs with his own beer label. I've attached the copy and put design specs below.
RATIONALE
My Dad is a cool guy, one of life’s absolute gems. He’s not a big drinker, but he likes a beer and he’s more likely to give them away at Christmas time than keep them in the fridge and drink them himself.
He’s also a master of Dad Jokes and offering pearls of wisdom, so combining a good beer with a funny Dad Joke or two on a can will be a great gift to give him for his birthday, Father’s Day or Christmas.
PLACEMENT
The front of the can needs to be my Dad’s head in cartoon form and GEDRIC’S LAGER has to be the most prominent wording.
While GEDRIC’S LAGER is the main heading…I’d like A TAMSWORTH RISE BREW up the top and GEDRIC’S LAGER IS LIFE’S BEER NECESSITY as the key wording wrapping around the bottom of the can.
I'd also like these sayings/jokes included (all of them OR as many that look cool and don't make the design too crowded):
“A beer in each hand is a balanced diet,” - Gedric

“This beer tastes like I’m not going to work tomorrow,” - Gedric

“Your beer isn’t half-full…it’s halfway to your next brew,” - Gedric

“My doc says I shouldn’t drink every day…that’s why I tend to drink at night,” - Gedric

“Two beer or not two beer,” - Shakesbeer

Why do frogs taste like beer?
Because of all the hops

What does Santa Claus drink?
A polar beer
Why do we like beer?
Coz you can’t drink bacon

Fat? Nah, beer makes you lean…
…against walls, doors…hotties

What's a beer’s favourite language?
Hebrew
DESIGN
Use the photos as a guide to turn my Dad (Gedric) into a cartoon - smiling/grinning, upbeat and happy. Not too old looking!
In terms of the can’s design, this is where I want YOU to be a design maestro. His head could burst through GEDRIC’S LAGER or simply have the lettering wrapped around his image.
Are the quotes and jokes in speech bubbles? Or are they in beer bubbles? Is a smaller version of Dad’s head used as a bullet point by each quote or joke?
FONT
Your choice! It just needs to be easy to read or and not too old-fashioned or - at the other extreme - too futuristic.
COLOUR
Your choice! He’s from a province that has red and black as their core colours, but if that doesn’t work, please go with a light teal/blue - or some other semi-masculine colour - and a dark colouring for the wording/lettering.
FORMAT
The approved copy needs to be provided as a PDF and a jpeg.
Maximum size is 250 MB
DIMENSIONS
160mm wide by 85mm high.

Target Market(s)

A target market of ONE - my Dad. I want him to LOVE his gift - his own personal beer can with his image and name on it.

Industry/Entity Type

Beer...

Colors

Designer to choose colors to be used in the design.

Requirements
Must have
• A fun, impactful BEER CAN design featuring my Dad's cartoon visage and some if not all of the Dad Jokes/beer sayings provided.

```html
<!DOCTYPE html>
<html lang="en">
<head>
<meta charset="utf-8">
<title>Gedric's Lager – Can Label</title>
<link rel="stylesheet" href="https://fonts.googleapis.com/css2?family=Tinos:wght@400;700&display=swap">
<style>
  :root {
    --brand-red: #d8131b;
    --band-red: #e0141c;
    --ink-white: #ffffff;
    --wood-dark: #121212;
    --wood-mid: #262626;
    --page: #ffffff;
    --portrait-a: #8a8f96;
    --portrait-b: #3d3f44;
  }
  * { box-sizing: border-box; margin: 0; padding: 0; }
  html, body { width: 865px; height: 1200px; overflow: hidden; background: var(--page); }
  body { font-family: "Tinos", "Times New Roman", serif; display: flex; align-items: center; justify-content: center; }

  .label {
    position: relative;
    width: 865px;
    height: 460px;
    background: linear-gradient(180deg, var(--wood-mid) 0%, var(--wood-dark) 50%, var(--wood-mid) 100%);
    overflow: hidden;
  }
  .band {
    position: absolute; left: 0; right: 0;
    background: var(--band-red);
    color: var(--ink-white);
    text-align: center;
    letter-spacing: 1px;
  }
  .band--top { top: 0; height: 48px; font-size: 24px; line-height: 50px; }
  .band--bottom { bottom: 0; height: 46px; font-size: 24px; line-height: 46px; }

  .portrait {
    position: absolute; left: 330px; top: 48px; width: 205px; height: 196px;
    background: radial-gradient(circle at 50% 45%, var(--portrait-a), var(--portrait-b) 75%, var(--wood-dark));
  }

  .brand {
    position: absolute; left: 0; right: 0; top: 254px;
    text-align: center; color: var(--brand-red);
    font-weight: 700;
  }
  .brand__name { font-size: 64px; line-height: 66px; letter-spacing: 1px; }
  .brand__sub { font-size: 22px; line-height: 26px; letter-spacing: 3px; }

  .quotes {
    position: absolute; left: 22px; top: 66px; width: 228px;
    list-style: none; color: var(--ink-white);
    font-size: 14px; line-height: 17px;
  }
  .quotes li { margin-bottom: 10px; }
  .quotes .who { color: var(--brand-red); }

  .jokes {
    position: absolute; left: 624px; top: 66px; width: 226px;
    list-style: none; color: var(--ink-white);
    font-size: 14px; line-height: 17px; font-weight: 700;
  }
  .jokes li { margin-bottom: 10px; }
  .jokes .answer { color: var(--brand-red); }
</style>
</head>
<body>
  <section class="label">
    <header class="band band--top">A TAMSWORTH RISE BREW</header>

    <ul class="quotes">
      <li>“A beer in each hand is a balanced diet,” - <span class="who">Gedric</span></li>
      <li>“This beer tastes like I’m not going to work tomorrow,” - <span class="who">Gedric</span></li>
      <li>“Your beer isn’t half-full…it’s halfway to your next brew,” - <span class="who">Gedric</span></li>
      <li>“My doc says I shouldn’t drink every day…that’s why I tend to drink at night,” - <span class="who">Gedric</span></li>
      <li>“Two beer or not two beer,” - <span class="who">Shakesbeer</span></li>
    </ul>

    <div class="portrait" role="img" aria-label="Portrait of Gedric, smiling, head and shoulders"></div>

    <div class="brand">
      <div class="brand__name">GEDRIC’S</div>
      <div class="brand__sub">LAGER</div>
    </div>

    <ul class="jokes">
      <li>Why do frogs taste like beer? <span class="answer">Because of all the hops</span></li>
      <li>What does Santa Claus drink? <span class="answer">A polar beer</span></li>
      <li>Why do we like beer? <span class="answer">Coz you can’t drink bacon</span></li>
      <li>Fat? Nah, beer makes you lean… <span class="answer">against walls, doors…hotties</span></li>
      <li>What’s a beer’s favourite language? <span class="answer">Hebrew</span></li>
    </ul>

    <footer class="band band--bottom">GEDRIC’S LAGER IS LIFE’S BEER NECESSITY</footer>
  </section>
</body>
</html>
```